Brantley Water Taxi and Transport

Need to redesign our business cards to relay that we do freight logistics and water taxi service. We also work with gov. agencies doing environmental clean up, oil spill response, remote site construction and work with many of the air taxi and helicopter services on Kodiak Island. Out website is www.brantleywatertaxi-example.com to get a better idea of what we do.

Contact Information for Business Card

I have a previous business card but it just has the logo on the front, and a sunset picture on the back with the contact info. It does not relay what we do and what we can help with. I like a simple straight forward design over a busy one.

Colors
3176b5
0455a3
cfdfed

Requirements
Must have
• logo, email, website, phone number

```html
<!DOCTYPE html>
<html lang="en">
<head>
<meta charset="utf-8">
<title>Brantley Water Taxi and Transport – Business Card</title>
<link rel="stylesheet" href="https://fonts.googleapis.com/css2?family=Roboto:ital,wght@0,400;0,500;0,700;1,400&display=swap">
<style>
  :root {
    --backdrop: #e4e4e4;
    --card-white: #ffffff;
    --brand-blue: #0a3aa8;
    --card-blue: #0033aa;
    --accent-orange: #f39c1a;
    --text-grey: #505050;
    --divider: #d6d6d6;
    --on-blue: #ffffff;
  }
  * { box-sizing: border-box; margin: 0; padding: 0; }
  html, body {
    width: 1125px;
    height: 1200px;
    overflow: hidden;
    background: var(--backdrop);
    font-family: "Roboto", Arial, sans-serif;
  }
  .canvas {
    position: relative;
    width: 1125px;
    height: 1200px;
  }
  .card {
    position: absolute;
    left: 153px;
    width: 825px;
    height: 471px;
    box-shadow: 0 4px 12px rgba(0, 0, 0, 0.25);
  }
  .card--front { top: 104px; background: var(--card-white); }
  .card--back  { top: 637px; background: var(--card-blue); }

  /* Front: company name block */
  .brand-name {
    position: absolute;
    left: 108px;
    top: 150px;
    width: 250px;
    text-align: center;
    color: var(--brand-blue);
    font-weight: 500;
    font-size: 27px;
    line-height: 1.25;
  }
  .divider {
    position: absolute;
    left: 387px;
    top: 139px;
    width: 1px;
    height: 200px;
    background: var(--divider);
  }
  .person {
    position: absolute;
    left: 425px;
    top: 146px;
  }
  .person__name {
    color: var(--brand-blue);
    font-weight: 700;
    font-size: 31px;
    line-height: 1;
    letter-spacing: 0.2px;
  }
  .person__title {
    color: var(--accent-orange);
    font-weight: 500;
    font-size: 21px;
    margin-top: 7px;
  }
  .contact-list {
    position: absolute;
    left: 425px;
    top: 238px;
    list-style: none;
  }
  .contact-list li {
    display: flex;
    align-items: center;
    height: 27px;
    color: var(--text-grey);
    font-size: 20px;
  }
  .contact-list svg {
    width: 18px;
    height: 18px;
    margin-right: 12px;
    fill: var(--brand-blue);
    flex: none;
  }

  /* Back */
  .back-brand {
    position: absolute;
    left: 510px;
    top: 305px;
    width: 270px;
    text-align: center;
    color: var(--on-blue);
    font-weight: 500;
    font-size: 25px;
    line-height: 1.25;
  }
  .back-web {
    position: absolute;
    right: 48px;
    top: 416px;
    color: var(--on-blue);
    font-style: italic;
    font-size: 19px;
  }
</style>
</head>
<body>
<main class="canvas">
  <section class="card card--front" aria-label="Card front">
    <div class="brand-name">Brantley Water Taxi and Transport</div>
    <div class="divider"></div>
    <div class="person">
      <div class="person__name">DANA WHITFIELD</div>
      <div class="person__title">CEO/FOUNDER</div>
    </div>
    <ul class="contact-list">
      <li>
        <svg viewBox="0 0 24 24" aria-hidden="true"><path d="M6.6 10.8a15.2 15.2 0 0 0 6.6 6.6l2.2-2.2a1 1 0 0 1 1-.25 11.4 11.4 0 0 0 3.6.57 1 1 0 0 1 1 1V20a1 1 0 0 1-1 1A17 17 0 0 1 3 4a1 1 0 0 1 1-1h3.5a1 1 0 0 1 1 1c0 1.25.2 2.45.57 3.57a1 1 0 0 1-.25 1z"/></svg>
        555 014 2790
      </li>
      <li>
        <svg viewBox="0 0 24 24" aria-hidden="true"><path d="M2 6h20v12H2z M3.5 7.5v.3L12 13l8.5-5.2v-.3z" fill-rule="evenodd"/></svg>
        dana@brantleywatertaxi-example.com
      </li>
      <li>
        <svg viewBox="0 0 24 24" aria-hidden="true"><circle cx="12" cy="12" r="10"/><path d="M7 8c2 0 3 1 3 3s-2 2-2 4 1 3 1 4c-2-1-4-3-4-6 0-2 1-4 2-5zM14 5c2 1 2 3 1 4s-2 0-2 2 2 2 3 1 2 0 2 2c-1 2-3 3-4 2" fill="#fff"/></svg>
        www.brantleywatertaxi-example.com
      </li>
    </ul>
  </section>

  <section class="card card--back" aria-label="Card back">
    <div class="back-brand">Brantley Water Taxi and Transport</div>
    <div class="back-web">www.brantleywatertaxi-example.com</div>
  </section>
</main>
</body>
</html>
```